Travel Blogger Business Card for roamquill.net

I need a two-sided business card for a travel blogging website. The card should be both professional and fun at the same time. This is for the website www.roamquill.net

I don't necessarily think that the current logo on the website needs to be used on the business card but it can be. I am very flexible with ideas

Target Market(s)

Travel agencies that will be met at a conference.

Industry/Entity Type

Travel

Contact Information for Business Card

Company Name: Roam Quill.net
Name: Bertrand Olesky
Voice: +1-(345)-402-7731
Address: Coral Reach Shore, Grand Cayman, Cayman Islands
Email: ceo@roamquill.net

Colors
0592cd
0355a3
3176b5
33a6d7
85cae6
85acd3

Requirements
Must have
• Website address and name should be bigger than address, phone number, and email.

```html
<!DOCTYPE html>
<html lang="en">
<head>
<meta charset="utf-8">
<title>Roam Quill – Business Card</title>
<link href="https://fonts.googleapis.com/css2?family=Lato:wght@400;700;900&display=swap" rel="stylesheet">
<style>
  :root {
    --blue-deep: #0355a3;
    --blue-mid: #3176b5;
    --blue-bright: #0592cd;
    --blue-sky: #33a6d7;
    --blue-pale: #85cae6;
    --blue-haze: #85acd3;
    --white: #ffffff;
    --stage: #e9ecf0;
  }
  * { box-sizing: border-box; margin: 0; padding: 0; }
  html, body {
    width: 1200px; height: 1000px; overflow: hidden;
    background: var(--stage);
    font-family: "Lato", Arial, sans-serif;
  }
  .card {
    position: absolute; left: 250px;
    width: 700px; height: 400px;
    border-radius: 28px; overflow: hidden;
    box-shadow: 0 10px 30px rgba(0,0,0,0.18);
  }
  /* Front */
  .card-front {
    top: 60px;
    background: radial-gradient(ellipse at 55% 40%, var(--blue-mid) 0%, var(--blue-deep) 75%);
  }
  .front-brand {
    position: absolute; left: 0; right: 0; top: 125px;
    display: flex; align-items: center; justify-content: center; gap: 16px;
  }
  .brand-dot {
    width: 44px; height: 44px; border-radius: 50%;
    background: var(--white);
  }
  .brand-name {
    font-weight: 900; font-size: 46px; letter-spacing: 0.5px;
    color: var(--white); text-transform: uppercase;
  }
  .front-band {
    position: absolute; left: 0; right: 0; top: 300px; height: 66px;
    background: var(--white);
    display: flex; align-items: center; justify-content: center;
  }
  .front-web {
    font-size: 20px; color: var(--blue-deep); font-weight: 400;
  }
  /* Back */
  .card-back { top: 540px; background: var(--blue-deep); }
  .back-shapes { position: absolute; inset: 0; }
  .back-brand {
    position: absolute; left: 460px; top: 122px;
    display: flex; align-items: center; gap: 10px;
  }
  .back-brand .brand-dot { width: 30px; height: 30px; background: var(--blue-bright); }
  .back-brand .brand-name { font-size: 30px; color: var(--blue-bright); }
  .contact {
    position: absolute; left: 48px; top: 150px; color: var(--white);
  }
  .contact-name { font-size: 30px; font-weight: 700; margin-bottom: 22px; }
  .contact-address { font-size: 16px; line-height: 1.3; margin-bottom: 18px; padding-left: 10px; }
  .contact-list { list-style: none; padding-left: 14px; }
  .contact-list li {
    display: flex; align-items: center; gap: 14px;
    font-size: 17px; margin-bottom: 8px;
  }
  .contact-list svg { width: 16px; height: 16px; fill: var(--white); flex: none; }
  .contact-list .web { font-size: 19px; }
</style>
</head>
<body>

<section class="card card-front" aria-label="Card front">
  <div class="front-brand">
    <span class="brand-dot"></span>
    <span class="brand-name">Roam Quill</span>
  </div>
  <div class="front-band">
    <span class="front-web">www.roamquill.net</span>
  </div>
</section>

<section class="card card-back" aria-label="Card back">
  <svg class="back-shapes" viewBox="0 0 700 400" preserveAspectRatio="none">
    <defs>
      <linearGradient id="back-blue" x1="0" y1="0" x2="0" y2="1">
        <stop offset="0" stop-color="#0b62b0"/>
        <stop offset="1" stop-color="#0355a3"/>
      </linearGradient>
    </defs>
    <rect width="700" height="400" fill="url(#back-blue)"/>
    <path d="M380,0 C355,170 440,320 610,400 L700,400 L700,0 Z" fill="var(--blue-bright)"/>
    <path d="M384,0 C368,170 470,320 660,400 L700,400 L700,0 Z" fill="var(--blue-haze)"/>
    <path d="M400,0 C385,175 500,310 700,370 L700,0 Z" fill="var(--white)"/>
  </svg>

  <div class="back-brand">
    <span class="brand-dot"></span>
    <span class="brand-name">Roam Quill</span>
  </div>

  <div class="contact">
    <p class="contact-name">Bertrand Olesky</p>
    <p class="contact-address">Coral Reach Shore, Grand Cayman,<br>Cayman Islands</p>
    <ul class="contact-list">
      <li>
        <svg viewBox="0 0 24 24"><path d="M6.6 10.8a15.1 15.1 0 0 0 6.6 6.6l2.2-2.2c.3-.3.7-.4 1-.2 1.1.4 2.3.6 3.6.6.6 0 1 .4 1 1V20c0 .6-.4 1-1 1A17 17 0 0 1 3 4c0-.6.4-1 1-1h3.5c.6 0 1 .4 1 1 0 1.3.2 2.5.6 3.6.1.3 0 .7-.2 1z"/></svg>
        <span>+1-(345)-402-7731</span>
      </li>
      <li>
        <svg viewBox="0 0 24 24"><path d="M2 11 22 2l-9 20-2-8z"/></svg>
        <span>ceo@roamquill.net</span>
      </li>
      <li>
        <svg viewBox="0 0 24 24"><path d="M12 2a10 10 0 1 0 0 20 10 10 0 0 0 0-20zm1 17.9V18h-2v-2l-5-5 .3-2.4A8 8 0 0 1 16 5.1V7h-3v3h3l2 3v3h1.4A8 8 0 0 1 13 19.9z"/></svg>
        <span class="web">www.roamquill.net</span>
      </li>
    </ul>
  </div>
</section>

</body>
</html>
```